Lanternfield Drinks business cards

We need a business card design for our new logo. The company is modern, progressive, professional, yet approachable. The key products are ready to drink bottles and cans of coffee based beverages.
These cards will be a critical part of the first impression made by our sales organization, business development team, and all external facing personnel.
Card can be a vertical or horizontal orientation.

Target Market(s)

Customers, suppliers, business partners

Industry/Entity Type

Business

Contact Information for Business Card

Business cards should feature Company Name and Logo.

Font styles to use
Serif

Colors

Designer to choose colors to be used in the design.

Requirements
Must have
• Strong readability of Name, phone #, mobile number and email address.
• Job title, website url, Street Address, and other details can be secondary level readability.
Nice to have
• High impact, simplistic quality design.
• Ok to utilize the 'H in the box' separate from the company name

```html
<!DOCTYPE html>
<html lang="en">
<head>
<meta charset="utf-8">
<title>Lanternfield Drinks – Business Cards</title>
<link rel="stylesheet" href="https://fonts.googleapis.com/css2?family=Tinos:wght@400;700&display=swap">
<style>
  :root {
    --backdrop: #9a7f60;
    --card: #ffffff;
    --card-shade: #f1f1f1;
    --brand: #e9582a;
    --ink: #2b2b2b;
    --ink-soft: #3d3d3d;
    --rule: #555555;
  }
  * { margin: 0; padding: 0; box-sizing: border-box; }
  html, body { width: 900px; height: 1200px; overflow: hidden; }
  body {
    position: relative;
    background: var(--backdrop);
    font-family: "Tinos", "Times New Roman", serif;
    color: var(--ink);
  }
  .card {
    position: absolute;
    left: 82px;
    width: 733px;
    height: 428px;
    border-radius: 22px;
    background: linear-gradient(135deg, var(--card) 40%, var(--card-shade));
    box-shadow: 0 4px 10px rgba(0,0,0,0.35);
  }
  .card--front { top: 137px; }
  .card--back { top: 632px; }

  .brand-mark {
    position: absolute;
    width: 78px; height: 78px;
    background: var(--brand);
  }
  .brand-name {
    position: absolute;
    font-weight: 700;
    color: var(--brand);
    text-transform: uppercase;
    text-align: center;
    white-space: nowrap;
    letter-spacing: 0.5px;
  }
  .card--front .brand-mark { left: 160px; top: 143px; }
  .card--front .brand-name {
    left: 66px; width: 267px; top: 232px;
    font-size: 28px; line-height: 32px;
  }
  .divider {
    position: absolute;
    left: 372px; top: 145px;
    width: 1px; height: 142px;
    background: var(--rule);
  }
  .contact { position: absolute; left: 408px; top: 136px; }
  .contact__name { font-size: 26px; font-weight: 400; color: var(--ink); line-height: 32px; }
  .contact__title { font-size: 15px; color: var(--brand); line-height: 20px; margin-bottom: 18px; }
  .contact__list { list-style: none; }
  .contact__item {
    display: flex; align-items: center;
    height: 29px;
    font-size: 16px; color: var(--ink-soft);
  }
  .contact__icon {
    width: 19px; height: 19px; margin-right: 12px;
    background: var(--brand); border-radius: 3px;
    display: flex; align-items: center; justify-content: center;
  }
  .address {
    position: absolute; left: 0; right: 0; top: 372px;
    text-align: center; font-size: 16px; color: var(--ink-soft);
  }

  .card--back .brand-mark { left: 310px; top: 116px; width: 108px; height: 108px; }
  .card--back .brand-name {
    left: 0; width: 733px; top: 242px;
    font-size: 38px; line-height: 44px;
  }
</style>
</head>
<body>
  <section class="card card--front">
    <div class="brand-mark"></div>
    <div class="brand-name">Lanternfield<br>Drinks</div>
    <div class="divider"></div>
    <div class="contact">
      <h1 class="contact__name">Marcus Hollander</h1>
      <p class="contact__title">Owner - Project Manager</p>
      <ul class="contact__list">
        <li class="contact__item">
          <span class="contact__icon">
            <svg width="13" height="13" viewBox="0 0 24 24"><path fill="#fff" d="M6.6 10.8a15.1 15.1 0 0 0 6.6 6.6l2.2-2.2a1 1 0 0 1 1-.25 11.4 11.4 0 0 0 3.6.57 1 1 0 0 1 1 1V20a1 1 0 0 1-1 1A17 17 0 0 1 3 4a1 1 0 0 1 1-1h3.5a1 1 0 0 1 1 1c0 1.25.2 2.45.57 3.57a1 1 0 0 1-.25 1z"/></svg>
          </span>555-014-2290
        </li>
        <li class="contact__item">
          <span class="contact__icon">
            <svg width="13" height="13" viewBox="0 0 24 24"><rect x="2" y="5" width="20" height="14" fill="none" stroke="#fff" stroke-width="2"/><path d="M2 5l10 8 10-8" fill="none" stroke="#fff" stroke-width="2"/></svg>
          </span>Ellenward@lanternfield.com
        </li>
        <li class="contact__item">
          <span class="contact__icon">
            <svg width="13" height="13" viewBox="0 0 24 24" fill="none" stroke="#fff" stroke-width="2"><circle cx="12" cy="12" r="9"/><path d="M3 12h18M12 3c3 3 3 15 0 18M12 3c-3 3-3 15 0 18"/></svg>
          </span>www.lanternfield.com
        </li>
      </ul>
    </div>
    <p class="address">2740 Alder Street, #118, Denver, CO 80205</p>
  </section>

  <section class="card card--back">
    <div class="brand-mark"></div>
    <div class="brand-name">Lanternfield Drinks</div>
  </section>
</body>
</html>
```